PowerPoint Template Design

We are an independent private equity and advisory firm (mergers and acquisitions), based in Brazil. We are looking for a power point template to use for companies presentations to investors and other targets (ie competitors).
Find attached the actual template that we use, we need something with this structure but more customized.

- Cover slide with our logo, project name and current date
- Index/Agenda slide
- Content slides
a. Slide with title, subtitle, text and footer. The footer should contain the page number, the person who we are sending to and the word "CONFIDENTIAL"
b. Slide with title, subtitle, text and pictures/charters/graphics
- Final slide with adress and contacts

We do not want something very colorful, we need something plain, simple but modern.

Target Market(s)

Investors, CEOs, CFOs, other advisory firms like TLHarwick, RZNB, Tallbrook, etc.

Industry/Entity Type

Equity

Requirements
Must have
• - the same colors used by our designer;
- one font only (Century Gothic);

```html
<!DOCTYPE html>
<html lang="en">
<head>
<meta charset="utf-8">
<title>Content Slide – Table</title>
<link href="https://fonts.googleapis.com/css2?family=Jura:wght@400;500&family=Carlito:wght@400;700&display=swap" rel="stylesheet">
<style>
  :root {
    --ink: #111111;
    --ink-soft: #3a3a3a;
    --header-fade-start: #e6e6e6;
    --header-fade-end: #ffffff;
    --table-head: #a6a6a6;
    --table-cell: #e9e8e9;
    --table-frame: #dcdcdc;
    --rule-dark: #4d4d4d;
    --accent: #ffae00;
    --white: #ffffff;
  }
  * { box-sizing: border-box; margin: 0; padding: 0; }
  html, body {
    width: 1200px; height: 900px; overflow: hidden; background: var(--white);
  }
  .slide {
    position: relative; width: 1200px; height: 900px; background: var(--white);
    font-family: "Carlito", "Calibri", sans-serif; color: var(--ink);
  }
  .slide-header {
    position: absolute; left: 0; top: 0; width: 1200px; height: 105px;
    background: linear-gradient(90deg, var(--header-fade-start) 0%, #f3f3f3 45%, var(--header-fade-end) 100%);
  }
  .slide-title {
    position: absolute; left: 56px; top: 26px;
    font-family: "Jura", sans-serif; font-weight: 500; font-size: 40px; letter-spacing: 1px;
    color: var(--ink);
  }
  .brand-top {
    position: absolute; right: 30px; top: 34px;
    font-family: "Carlito", sans-serif; font-size: 30px; letter-spacing: 8px; color: var(--ink-soft);
  }
  .section-title {
    position: absolute; left: 56px; top: 183px;
    font-family: "Jura", sans-serif; font-weight: 500; font-size: 33px; color: var(--ink-soft);
  }
  .data-table {
    position: absolute; left: 57px; top: 261px; width: 1032px;
    border: 1px solid var(--table-frame); box-shadow: 0 0 4px rgba(0,0,0,0.12);
    padding: 4px; background: var(--white);
    border-collapse: separate; border-spacing: 3px;
    display: grid; grid-template-columns: 339px 339px 339px; gap: 3px;
  }
  .cell {
    height: 66px; padding-left: 18px; display: flex; align-items: center;
    background: var(--table-cell); font-size: 21px; color: var(--ink-soft);
  }
  .cell--head { background: var(--table-head); color: var(--white); font-size: 25px; }
  .slide-footer {
    position: absolute; left: 0; top: 844px; width: 1200px; height: 56px;
    border-top: 6px solid var(--rule-dark); background: var(--accent);
  }
  .page-number {
    position: absolute; left: 38px; top: 10px;
    font-weight: 700; font-size: 21px; color: var(--white);
  }
  .brand-footer {
    position: absolute; right: 16px; top: 8px;
    font-family: "Carlito", sans-serif; font-size: 30px; letter-spacing: 9px; color: var(--ink);
  }
</style>
</head>
<body>
  <main class="slide">
    <header class="slide-header">
      <h1 class="slide-title">Persentation Title Here</h1>
      <div class="brand-top">VALORE</div>
    </header>

    <h2 class="section-title">Table Content here</h2>

    <section class="data-table" aria-label="Content table">
      <div class="cell cell--head">Heading Content</div>
      <div class="cell cell--head">Heading Content</div>
      <div class="cell cell--head">Heading Content</div>
      <div class="cell">Sub Content Here</div>
      <div class="cell">Sub Content Here</div>
      <div class="cell">Sub Content Here</div>
      <div class="cell">Sub Content Here</div>
      <div class="cell">Sub Content Here</div>
      <div class="cell">Sub Content Here</div>
      <div class="cell">Sub Content Here</div>
      <div class="cell">Sub Content Here</div>
      <div class="cell">Sub Content Here</div>
    </section>

    <footer class="slide-footer">
      <span class="page-number">Page : 01</span>
      <span class="brand-footer">VALORE</span>
    </footer>
  </main>
</body>
</html>
```